Cleaning service website design

We need a new nice web design(logo will be the same) for a new cleaning service Company:

Informations about Company and logo you can take from flyers in attachments.

This is a cleaning service Company which have simple rules and we would like to show that(in checklist form) on website:

- What we do and that we're Cleaning Green

- Why us?

- How much(our pricing is simple)

Also we would like to communicate with clients by some nice/big pictures on website and the most important thing is our phone number and short/fast Freestimate.

Also there should be some space for description about our Company.

Generally all information on main page can be short: about us, about service(what we do), last reviews, tips (for example: Tip of the week) and other can be some introduction to subpage where will be more information.

There will be few subpages like: About us, About our service, Photos(Before and after), Reviews , Tips, FAQ, Contact, Looking for a Job? - most of them will be just text so you can project just one example.

```html
<!DOCTYPE html>
<html lang="en">
<head>
<meta charset="utf-8">
<title>Tidy Nest House Cleaning</title>
<link href="https://fonts.googleapis.com/css2?family=Alegreya:wght@500;700&family=Arvo:wght@700&family=Bebas+Neue&family=Kalam:wght@700&family=Lato:ital,wght@0,400;1,400&family=Oswald:wght@400;500&family=Pathway+Gothic+One&display=swap" rel="stylesheet">
<style>
:root{
  --blue:#0a5cad;
  --navy:#0e2f55;
  --green:#7cc453;
  --green-dark:#4f9e2c;
  --green-field:#a8da8a;
  --sky:#9dc3e6;
  --cta:#9ec6ec;
  --ink:#2a2a2a;
  --pill:#eef2f6;
}
*{margin:0;padding:0;box-sizing:border-box}
html,body{width:791px;height:1200px;overflow:hidden;background:#fff}
.page{position:absolute;left:0;top:0;width:980px;height:1487px;transform:scale(0.80714);transform-origin:0 0;font-family:Arial,Helvetica,sans-serif;background:#fff}
.abs{position:absolute}

/* header */
.brand{left:10px;top:22px;display:flex;align-items:center;gap:10px}
.brand-dot{width:40px;height:40px;border-radius:50%;background:var(--blue)}
.brand-name{font-family:'Alegreya',serif;font-weight:700;font-size:25px;color:var(--blue);white-space:nowrap}
.social{right:12px;top:10px;display:flex;gap:10px}
.social span{width:22px;height:22px;border-radius:50%;background:var(--green)}
.nav{left:180px;top:45px;width:800px;height:38px;background:var(--blue)}
.nav a{position:absolute;top:9px;color:#fff;text-decoration:none;font-family:'Alegreya',serif;font-weight:500;font-size:16px;white-space:nowrap}

/* sidebar */
.sidebar{left:4px;top:110px;width:174px;height:1315px;background:var(--green);border-radius:22px 0 0 0}
.sb-title{position:absolute;left:16px;font-family:'Bebas Neue',sans-serif;font-size:33px;color:#fff;letter-spacing:-.5px;white-space:nowrap}
.field{position:absolute;left:12px;width:149px;height:26px;background:var(--green-field);border:1px solid #c5e8b1;border-radius:4px;font-size:11.5px;font-weight:bold;color:#2f7f16;padding:6px 8px}
.submit{position:absolute;left:13px;top:686px;width:68px;height:22px;background:var(--green-dark);border:1px solid #c5e8b1;border-radius:5px;color:#fff;font-size:11.5px;font-weight:bold;text-align:center;line-height:20px}
.tip-img{position:absolute;left:12px;top:776px;width:150px;height:198px;background:linear-gradient(135deg,#2f8fe0,#bfe4fb 55%,#f2d23b);border:2px solid #d8efc8}
.tip-text{position:absolute;left:13px;top:988px;width:152px;color:#fff;font-size:11.5px;line-height:14.4px}

/* hero */
.hero{left:180px;top:83px;width:800px;height:300px;background:linear-gradient(160deg,#e9e2d8,#c9a277 55%,#b78b5f)}
.wave{left:180px;top:330px;width:800px;height:100px}
.need{left:180px;top:352px;width:800px;text-align:center;font-family:'Kalam',cursive;font-size:40px;color:#fff;letter-spacing:1px}
.simple{left:194px;top:391px;font-family:'Pathway Gothic One',sans-serif;font-size:28px;color:#fff;white-space:nowrap}
.hero-phone{right:12px;top:387px;display:flex;align-items:center;gap:8px;font-family:'Oswald',sans-serif;font-weight:500;font-size:31px;line-height:40px;color:#fff;white-space:nowrap}

/* features */
.features{left:180px;top:430px;width:800px;height:995px;background:var(--blue)}
.card-l,.card-r{position:absolute;top:430px;height:290px;background:#fff}
.card-l{left:180px;width:403px;border-radius:0 40px 60px 0/0 40px 40px 0;box-shadow:inset -14px 0 16px -12px #d6d6d6}
.card-r{left:584px;width:396px;border-radius:40px 0 0 60px/40px 0 0 40px;box-shadow:inset 14px 0 16px -12px #d6d6d6}
.card-title{position:absolute;top:474px;font-family:'Arvo',serif;font-weight:700;font-size:31px;color:var(--ink);white-space:nowrap}
.checks{position:absolute;list-style:none;font-family:'Pathway Gothic One',sans-serif;font-size:21px;line-height:21.7px;color:#333}
.checks li{position:relative;padding-left:28px}
.checks li::before{content:"";position:absolute;left:0;top:6px;border-left:12px solid var(--green-dark);border-top:5px solid transparent;border-bottom:5px solid transparent}

/* about */
.h2{position:absolute;font-family:'Lato',sans-serif;font-size:31px;color:#fff}
.tagline{left:221px;top:812px;font-family:'Lato',sans-serif;font-style:italic;font-size:17px;color:#fff}
.about-p{left:221px;top:854px;width:335px;font-size:14.4px;line-height:17px;color:#fff}
.more{left:221px;top:951px;width:90px;height:22px;background:var(--green);border-radius:11px;color:var(--blue);font-size:11.5px;font-weight:bold;line-height:22px;padding-left:9px}
.quote{position:absolute;left:221px;width:275px;font-size:12px;line-height:14.5px;color:#fff}
.quote b{display:block;margin-top:8px}

/* pricing */
.pcard{position:absolute;left:650px;width:302px;background:#fff;border-radius:8px;text-align:center}
.p-head{font-family:'Lato',sans-serif;font-size:23px;color:var(--blue)}
.big{font-family:'Oswald',sans-serif;font-weight:500;white-space:nowrap}
.ring{position:absolute;width:24px;height:56px;border-radius:12px;background:var(--navy);border:3px solid #d8dee6}
.row{width:280px;height:30px;margin:0 auto 5px;background:var(--pill);border-radius:5px;font-family:'Alegreya',serif;font-weight:500;font-size:16.5px;color:var(--blue);line-height:30px}
.cta{left:180px;top:1354px;width:800px;text-align:center;padding-left:20px;font-family:'Alegreya',serif;font-weight:500;font-size:23px;color:var(--cta);white-space:nowrap}

/* footer */
.footer{left:4px;top:1425px;width:976px;height:62px;background:var(--sky)}
.footer a{position:absolute;top:27px;font-family:'Alegreya',serif;font-weight:700;font-size:12.5px;color:var(--blue);text-decoration:none;white-space:nowrap}
.copy{position:absolute;left:573px;top:26px;font-family:'Alegreya',serif;font-weight:700;font-size:12.5px;color:var(--blue);white-space:nowrap}
.f-brand{position:absolute;left:900px;top:25px;font-family:'Alegreya',serif;font-weight:700;font-size:15px;color:var(--blue);white-space:nowrap}
</style>
</head>
<body>
<div class="page">

  <header>
    <div class="abs brand"><span class="brand-dot"></span><span class="brand-name">Tidy Nest</span></div>
    <div class="abs social" aria-label="Social links"><span></span><span></span><span></span><span></span></div>
    <nav class="abs nav">
      <a style="left:29px">About us</a><a style="left:129px">Services</a><a style="left:225px">Photos</a><a style="left:309px">Reviews</a><a style="left:405px">Tips</a><a style="left:474px">FAQ</a><a style="left:544px">Contact</a><a style="left:638px">Looking for a Job?</a>
    </nav>
  </header>

  <aside class="abs sidebar">
    <div class="sb-title" style="top:22px">FREE ESTIMATE</div>
    <div class="field" style="top:67px">full name</div>
    <div class="field" style="top:107px">complete address</div>
    <div class="field" style="top:147px">city</div>
    <div class="field" style="top:187px">state/province</div>
    <div class="field" style="top:227px">zip/postal code</div>
    <div class="field" style="top:267px">phone</div>
    <div class="field" style="top:307px">email</div>
    <div class="field" style="top:348px;height:157px">how did you hear<br>about us?</div>
    <div class="field" style="top:518px;height:157px">comments</div>
    <div class="submit">submit</div>
    <div class="sb-title" style="top:734px;left:12px">TIP OF THE WEEK</div>
    <div class="tip-img" role="img" aria-label="Photo of a smiling cleaner holding cleaning supplies"></div>
    <div class="tip-text">Lorem ipsum dolor sit amet, consectetur adipisicing elit, sed do eiusmod tempor incididunt ut labore et dolore magna aliqua. Ut enim ad minim veniam, quis nostrud exercitation ullamco laboris nisi ut aliquip ex ea commodo consequat.<br><br>Duis aute irure dolor in reprehenderit in voluptate velit esse cillum dolore eu fugiat nulla pariatur. Excepteur sint occaecat cupidatat non proident, sunt in culpa qui officia deserunt mollit anim id est laborum.</div>
  </aside>

  <section>
    <div class="abs hero" role="img" aria-label="Photo of a stressed homeowner in a messy living room with a vacuum and scattered laundry"></div>
    <svg class="abs wave" viewBox="180 330 800 100" aria-hidden="true">
      <path d="M180 378 L360 378 C420 378 440 338 580 338 C720 338 740 378 800 378 L980 378 L980 430 L180 430 Z" fill="#7cc453"/>
      <path d="M180 386 L400 386 C470 386 480 420 560 420 C650 420 690 390 760 388 L980 386 L980 430 L180 430 Z" fill="#0a5cad"/>
    </svg>
    <div class="abs need">Need Help?</div>
    <div class="abs simple">Its simple... call today!</div>
    <div class="abs hero-phone">
      <svg width="32" height="32" viewBox="0 0 32 32" aria-hidden="true"><circle cx="16" cy="16" r="14" fill="none" stroke="#fff" stroke-width="2.5"/><path d="M11 9c-2 1-2 4 0 7s5 6 8 7c2 0 3-1 3-2l-3-3-2 1c-2-1-3-3-4-4l1-2-3-4z" fill="#fff"/></svg>
      <span>555-014-2290</span>
    </div>
  </section>

  <div class="abs features"></div>
  <section>
    <div class="card-l"></div>
    <div class="card-r"></div>
    <h2 class="card-title" style="left:210px">Why choose us?</h2>
    <ul class="checks" style="left:216px;top:522px">
      <li>Owners Present at Every Cleaning</li><li>Locally Owned &amp; Operated</li><li>Reliable &amp; Affordable</li><li>All Supplies Provided</li><li>Green Cleaning</li><li>Pet Friendly</li><li>No Contracts</li>
    </ul>
    <h2 class="card-title" style="left:665px">What do we do?</h2>
    <ul class="checks" style="left:671px;top:522px;width:260px">
      <li>Thoroughly clean your bathrooms, kitchen, bedrooms and living areas</li><li>Mop or vacuum your floors</li><li>Dust surfaces</li><li>Collect garbage</li><li>Make beds</li>
    </ul>
  </section>

  <section>
    <h2 class="h2" style="left:222px;top:768px">ABOUT US</h2>
    <div class="abs tagline">It’s about caring, not just cleaning.</div>
    <p class="abs about-p">Having personally experienced the struggles of finding quality maid service for our home, we want to make it simpler for families in the Brookfield area. Our goal is to provide caring, consistent and reliable house cleaning to every customer we serve</p>
    <div class="abs more">learn more ▸</div>
    <h2 class="h2" style="left:222px;top:1009px">TESTIMONIALS</h2>
    <div class="quote" style="top:1058px">“The service is good, they left my house very clean, no evidence of dirt, my bathroom looks new and my bed wow. They really did a great job on what they do”<b>by: Dana Whitfield</b></div>
    <div class="quote" style="top:1168px">“The service is good, they left my house very clean, no evidence of dirt, my bathroom looks new and my bed wow. They really did a great job on what they do”<b>by: Dana Whitfield</b></div>
  </section>

  <section>
    <div class="pcard" style="top:770px;height:148px;padding-top:10px">
      <div class="p-head">HOUSE CLEANING</div>
      <div style="color:var(--green-dark);margin-top:2px"><span style="font-size:13px;vertical-align:14px">as low as </span><span class="big" style="font-size:47px;color:var(--green)">$79.00</span></div>
      <div style="font-size:12px;color:var(--blue)">*rates are for regular service* <span style="color:var(--green-dark)">&nbsp;PROMO: TDNS13</span></div>
    </div>
    <div class="pcard" style="top:927px;height:148px;padding-top:30px">
      <div class="p-head" style="color:#222">CALL NOW!</div>
      <div style="display:flex;justify-content:center;align-items:center;gap:10px;margin-top:4px;height:52px">
        <svg width="48" height="48" viewBox="0 0 32 32" aria-hidden="true"><circle cx="16" cy="16" r="14" fill="none" stroke="#1b1b1b" stroke-width="2"/><path d="M11 9c-2 1-2 4 0 7s5 6 8 7c2 0 3-1 3-2l-3-3-2 1c-2-1-3-3-4-4l1-2-3-4z" fill="#1b1b1b"/></svg>
        <span class="big" style="font-size:37px;line-height:48px;color:#1b1b1b">555-014-2290</span>
      </div>
    </div>
    <div class="pcard" style="top:1083px;height:230px;padding-top:43px">
      <div class="row">$79 for homes less than 1000 sq ft</div>
      <div class="row">$89 for homes 1000-1800 sq ft</div>
      <div class="row">$99 for homes 1800-2600 sq ft</div>
      <div style="font-size:13.5px;color:var(--green-dark);margin-top:6px;line-height:17px">*If your home is larger than 2600 sq ft<br>please call for a quote.</div>
      <div style="font-size:12px;color:var(--blue);margin-top:10px">*rates are for regular service*</div>
    </div>
    <div class="ring" style="left:710px;top:893px"></div><div class="ring" style="left:880px;top:893px"></div>
    <div class="ring" style="left:710px;top:1050px"></div><div class="ring" style="left:880px;top:1050px"></div>
    <div class="abs cta">CALL 555-014-2290 or fill out the form to the right to simplify your life!</div>
  </section>

  <footer class="abs footer">
    <a style="left:17px">About us</a><a style="left:74px">Services</a><a style="left:129px">Photos</a><a style="left:176px">Reviews</a><a style="left:230px">Tips</a><a style="left:263px">FAQ</a><a style="left:296px">Contact</a><a style="left:351px">Looking for a Job?</a>
    <div class="copy">© 2012 Tidy Nest House Cleaning. All rights reserved.</div>
    <div class="f-brand">Tidy Nest</div>
  </footer>

</div>
</body>
</html>
```